New high end server provider needs wordpress design

www.kv7hostrack.com

Need a wordpress design for a high end server provider that provides overclocked dedicated servers for rent. We are located in Chicago but we have a presence is Virginia and Nevada for both our east and west coast customers.

We are a server provider that specializes in top end hardware with every feature designed for optimum performance. If it is not the best quality part or provides the best possible performance we don't run it. Our customers are mainly those that want the best single threaded performance possible from their hardware. We would be selling our services directly on our website via WHMCS.

We would like to see designs that are very modern and simplistic yet very attractive looking and catchy. Would prefer colors in the blues and greens and white. These colors are not necessary and I would be open to another color scheme if it looks good.

The final design should show speed and performance while being simplistic and easy on the eyes.
Updates

Logo and company name added and payment changed to guaranteed.  Looking for a wordpress template with the same pages as kv7hostrack.com but with a redesigned look and feel.  

WHMCS control panel design also part of the design request.

If you have any questions please let me know!  This is just for kv7hostrack.com and a main page for WHMCS (no coding just design).

Target Market(s)

IT Guru's (mostly men in their 20's to 30's)

Industry/Entity Type

Hardware

Requirements
Must have
• WHMCS panel design to fit with website theme.
Nice to have
• Main slider on home page similar to one of our other websites at www.kv7hostrack.com
Should not have
• Flash or frames

```html
<!DOCTYPE html>
<html lang="en">
<head>
<meta charset="utf-8">
<title>KV7 Host Rack</title>
<link href="https://fonts.googleapis.com/css2?family=Arimo:wght@400;700&family=Carlito:wght@400;700&family=Tinos:wght@400;700&display=swap" rel="stylesheet">
<style>
:root{
  --page:#d9d9d9;
  --page-top:#c9c9c9;
  --blue-hi:#0c8cf5;
  --blue-lo:#0050b4;
  --navy:#003f8c;
  --navy-dark:#00357a;
  --panel:#ffffff;
  --ink:#111111;
  --text:#555555;
  --rule:#e2e2e2;
  --green-hi:#5bb32a;
  --green-lo:#2d7a0c;
  --btn-hi:#a9acb1;
  --btn-lo:#6d7076;
  --footer-link:#a8bede;
}
*{margin:0;padding:0;box-sizing:border-box}
html,body{width:1200px;height:1171px;overflow:hidden}
body{position:relative;background:linear-gradient(var(--page-top),var(--page) 40px);font-family:"Arimo",Arial,sans-serif;color:var(--text)}
.abs{position:absolute}
.blue-band{left:0;top:102px;width:1200px;height:246px;background:linear-gradient(var(--blue-hi),var(--blue-lo));box-shadow:0 8px 10px rgba(0,0,0,.18)}
.footer-band{left:0;top:1006px;width:1200px;height:165px;background:var(--navy)}
.footer-base{left:0;top:1120px;width:1200px;height:51px;background:var(--navy-dark);border-top:1px solid #0a4a9a}
.logo{left:254px;top:24px;font-family:"Tinos",serif;font-weight:700;font-size:31px;color:#444;letter-spacing:1px}
.nav{left:248px;top:79px;width:708px;height:32px;border-radius:8px;background:linear-gradient(#fafafa,#dcdcdc);display:flex;align-items:stretch;padding-left:26px;box-shadow:0 1px 2px rgba(0,0,0,.2)}
.nav a{font-family:"Tinos",serif;font-weight:700;font-size:12px;color:#666;text-decoration:none;display:flex;align-items:center;padding:0 19px;letter-spacing:.3px}
.nav a.active{background:linear-gradient(#d4d4d4,#bcbcbc);color:#111}
.slider{left:248px;top:119px;width:706px;height:257px;border-radius:5px;overflow:hidden;background:linear-gradient(#5d7089,#c5cfdb);box-shadow:0 6px 6px rgba(0,0,0,.25)}
.slide-art{position:absolute;left:455px;top:29px;width:145px;height:200px;background:linear-gradient(90deg,#1b1d20,#3d4146);border-radius:4px}
.caption{position:absolute;left:0;top:188px;width:706px;height:69px;background:rgba(225,228,232,.82)}
.caption h2{position:absolute;left:54px;top:11px;font-size:19px;font-weight:700;color:#333}
.caption p{position:absolute;left:54px;top:37px;font-size:11px;color:#111}
.arrow{position:absolute;top:19px;width:30px;height:24px;border-radius:12px;background:linear-gradient(#fff,#ddd);box-shadow:0 1px 2px rgba(0,0,0,.3)}
.arrow svg{position:absolute;left:9px;top:6px}
.panel{left:248px;top:408px;width:708px;height:636px;background:var(--panel);border-radius:4px;box-shadow:0 0 6px rgba(0,0,0,.25)}
.heading{position:absolute;font-size:19px;font-weight:700;color:var(--ink);border-bottom:1px solid var(--rule);padding-bottom:4px}
.copy{position:absolute;font-size:9.1px;line-height:10.4px;text-align:justify;color:var(--text)}
.copy p{margin-bottom:10.4px}
.learn{position:absolute;left:15px;top:257px;width:115px;height:26px;border-radius:13px;background:linear-gradient(var(--green-hi),var(--green-lo));color:#fff;font-weight:700;font-size:13px;display:flex;align-items:center;padding-left:14px;border:1px solid #1f5a06}
.learn i{position:absolute;right:6px;top:7px;width:11px;height:11px;border-radius:50%;background:#222}
.updates{position:absolute;left:479px;top:78px;width:202px}
.update{font-size:9.1px;line-height:10.4px;text-align:justify;color:var(--text);padding-bottom:5px;margin-bottom:9px;border-bottom:1px dashed #999}
.btn{position:absolute;width:113px;height:24px;border-radius:3px;background:linear-gradient(var(--btn-hi),var(--btn-lo));font-family:"Tinos",serif;font-size:14px;color:#222;display:flex;align-items:center;justify-content:center;box-shadow:0 1px 2px rgba(0,0,0,.3)}
.divider{position:absolute;left:10px;top:299px;width:688px;height:2px;background:linear-gradient(90deg,transparent,#ddd,transparent)}
.feature-title{position:absolute;display:flex;align-items:center;gap:4px;font-size:14.5px;font-weight:700;color:var(--ink)}
.feature-copy{position:absolute;width:214px;font-family:"Carlito",sans-serif;font-size:8.6px;line-height:10.4px;text-align:justify;color:#333}
.feature-copy p{margin-bottom:10.4px}
.partners{position:absolute;left:10px;top:594px;width:688px;border-top:1px solid var(--rule);height:42px}
.partner{position:absolute;top:11px;font-weight:700;font-size:16px;color:#222}
.footer-links{left:253px;top:1074px;font-size:9.5px;line-height:15px;color:var(--footer-link)}
.social{top:1070px;width:34px;height:34px;border-radius:4px;background:linear-gradient(#2b4f86,#0f2f5e);border:1px solid #5f7fb0;color:#dbe6f6;font-size:7px;display:flex;align-items:center;justify-content:center}
.copyright{left:0;top:1135px;width:1200px;text-align:center;font-size:9px;color:#8aa4cc}
</style>
</head>
<body>
<div class="abs blue-band"></div>
<div class="abs footer-band"></div>
<div class="abs footer-base"></div>

<div class="abs logo">LOGO</div>

<nav class="abs nav">
  <a class="active">HOME</a><a>OUR SERVERS</a><a>CLIENT AREA</a><a>WHY US?</a><a>TESTIMONIALS</a><a>CONTACTS</a>
</nav>

<section class="abs slider">
  <div class="slide-art" role="img" aria-label="Black tower server illustration"></div>
  <div class="caption">
    <div class="arrow" style="left:10px"><svg width="12" height="12" viewBox="0 0 12 12"><path d="M8 1 L3 6 L8 11" stroke="#111" stroke-width="2.2" fill="none"/></svg></div>
    <h2>Data Centers Located in &nbsp;Chicago, Virginia and Nevada</h2>
    <p>Nemo enim ipsam voluptatem quia voluptas sit aspernatur aut odit aut fugit, sed quia consequuntur magni dolores.</p>
    <div class="arrow" style="left:662px"><svg width="12" height="12" viewBox="0 0 12 12"><path d="M4 1 L9 6 L4 11" stroke="#111" stroke-width="2.2" fill="none"/></svg></div>
  </div>
</section>

<main class="abs panel">
  <h3 class="heading" style="left:17px;top:40px;width:440px">&nbsp;Welcome</h3>
  <div class="copy" style="left:17px;top:78px;width:440px">
    <p>Lorem ipsum dolor sit amet, consectetur adipiscing elit. Cras rhoncus consectetur dui, ac tincidunt tortor aliquam id. Nam non purus et erat ultrices suscipit id at lorem. Curabitur vestibulum metus a libero luctus hendrerit. Nunc diam enim, ullamcorper id mollis nec, dictum quis lacus. Nam vehicula porta nunc, ornare tristique ante euismod et.</p>
    <p>Suspendisse vel pellentesque nisl. Maecenas ante quam, sollicitudin eu ultricies quis, dignissim quis lectus. Sed eget luctus eros. Pellentesque vestibulum, sem quis aliquam aliquet, augue nisi pretium odio, vitae auctor eros tellus eu odio. Integer sollicitudin neque nec orci consequat eu tristique neque commodo. Proin libero quam, iaculis tristique pellentesque ut, interdum ac risus. Donec sapien augue, aliquam eget tincidunt eget, interdum vitae purus. Fusce venenatis pharetra pretium. Etiam pharetra nisi elementum neque iaculis eu laoreet lorem pellentesque .</p>
    <p>Vestibulum varius rutrum viverra. Nullam risus urna, vulputate vel feugiat sed, suscipit ut felis. Nunc interdum mauris ut nulla pellentesque viverra. Fusce tempus magna in lectus pretium euismod.</p>
  </div>
  <div class="learn">Learn More<i></i></div>

  <h3 class="heading" style="left:479px;top:40px;width:202px">Lates Update</h3>
  <div class="updates">
    <div class="update">Vestibulum varius rutrum viverra. Nullam risus urna, vulputate vel feugiat sed, suscipit ut felis. Nunc interdum mauris ut nulla pellentesque viverra.</div>
    <div class="update">Vestibulum varius rutrum viverra. Nullam risus urna, vulputate vel feugiat sed, suscipit ut felis. Nunc interdum mauris ut nulla pellentesque viverra.</div>
    <div class="update">Vestibulum varius rutrum viverra. Nullam risus urna, vulputate vel feugiat sed, suscipit ut felis. Nunc interdum mauris ut nulla pellentesque viverra.</div>
  </div>
  <div class="btn" style="left:481px;top:257px">View Another</div>

  <div class="divider"></div>

  <div class="feature-title" style="left:22px;top:344px">
    <svg width="22" height="32" viewBox="0 0 22 32"><rect x="2" y="1" width="18" height="30" rx="2" fill="#222"/><rect x="5" y="6" width="12" height="1.5" fill="#888"/><rect x="5" y="10" width="12" height="1.5" fill="#888"/></svg>Our Servers</div>
  <div class="feature-copy" style="left:13px;top:393px">
    <p>Lorem ipsum dolor sit amet, consectetur adipiscing elit. Cras rhoncus consectetur dui, ac tincidunt tortor aliquam id. Nam non purus et erat ultrices suscipit id at lorem. Curabitur vestibulum metus a libero luctus hendrerit.</p>
    <p>Nunc diam enim, ullamcorper id mollis nec, dictum quis lacus. Nam vehicula porta nunc, ornare tristique ante euismod et. Suspendisse vel pellentesque nisl. Maecenas ante quam, sollicitudin eu ultricies quis, dignissim quis lectus. Sed eget luctus eros. Pellentesque vestibulum, sem quis aliquam aliquet, augue nisi pretium odio, vitae auctor eros tellus eu odio.</p>
  </div>
  <div class="btn" style="left:15px;top:537px">View Another</div>

  <div class="feature-title" style="left:246px;top:344px">
    <svg width="28" height="28" viewBox="0 0 28 28"><g fill="#111"><circle cx="11" cy="15" r="7"/><g stroke="#111" stroke-width="3"><path d="M11 5v20M1 15h20M4 8l14 14M18 8L4 22"/></g><circle cx="21" cy="7" r="4"/><path d="M21 1v12M15 7h12" stroke="#111" stroke-width="2"/></g><circle cx="11" cy="15" r="2.5" fill="#fff"/><circle cx="21" cy="7" r="1.5" fill="#fff"/></svg>Our Services</div>
  <div class="feature-copy" style="left:245px;top:393px">
    <p>Lorem ipsum dolor sit amet, consectetur adipiscing elit. Cras rhoncus consectetur dui, ac tincidunt tortor aliquam id. Nam non purus et erat ultrices suscipit id at lorem. Curabitur vestibulum metus a libero luctus hendrerit.</p>
    <p>Nunc diam enim, ullamcorper id mollis nec, dictum quis lacus. Nam vehicula porta nunc, ornare tristique ante euismod et. Suspendisse vel pellentesque nisl. Maecenas ante quam, sollicitudin eu ultricies quis, dignissim quis lectus. Sed eget luctus eros. Pellentesque vestibulum, sem quis aliquam aliquet, augue nisi pretium odio, vitae auctor eros tellus eu odio.</p>
  </div>
  <div class="btn" style="left:247px;top:537px">View Another</div>

  <div class="feature-title" style="left:479px;top:346px">
    <svg width="26" height="24" viewBox="0 0 26 24"><path d="M13 1C6 1 1 5 1 10c0 3 2 5 4 7l-2 6 6-4c1 0 3 1 4 1 7 0 12-4 12-10S20 1 13 1z" fill="#111"/><text x="13" y="15" font-family="Arimo,sans-serif" font-size="12" font-weight="700" fill="#fff" text-anchor="middle">?</text></svg>Support</div>
  <div class="feature-copy" style="left:477px;top:393px">
    <p>Lorem ipsum dolor sit amet, consectetur adipiscing elit. Cras rhoncus consectetur dui, ac tincidunt tortor aliquam id. Nam non purus et erat ultrices suscipit id at lorem. Curabitur vestibulum metus a libero luctus hendrerit.</p>
    <p>Nunc diam enim, ullamcorper id mollis nec, dictum quis lacus. Nam vehicula porta nunc, ornare tristique ante euismod et. Suspendisse vel pellentesque nisl. Maecenas ante quam, sollicitudin eu ultricies quis, dignissim quis lectus. Sed eget luctus eros. Pellentesque vestibulum, sem quis aliquam aliquet, augue nisi pretium odio, vitae auctor eros tellus eu odio.</p>
  </div>
  <div class="btn" style="left:480px;top:536px">View Another</div>

  <div class="partners">
    <span class="partner" style="left:12px">Northvane</span>
    <span class="partner" style="left:150px">Kernelo</span>
    <span class="partner" style="left:236px">Intera</span>
    <span class="partner" style="left:310px">Corvan</span>
    <span class="partner" style="left:390px">Teramod</span>
  </div>
</main>

<nav class="abs footer-links">
  Home | Our Servers | Client Area | Why Us? | &nbsp;Testimonials | Contact<br>
  Privacy Policy | Terms of use
</nav>

<div class="abs social" style="left:774px">Facely</div>
<div class="abs social" style="left:822px">Chirpa</div>
<div class="abs social" style="left:871px">Linkwork</div>
<div class="abs social" style="left:919px">Viewcast</div>

<div class="abs copyright">Copyright 2013. All Rights Reserved.</div>
</body>
</html>
```